Großflächiges Banner-Design (Outdoor) für Karosserie & Autolackiererei
Karosserie & Autolackiererei Meisterbetrieb
Unfallinstandsetzung
Fehlerdiagnose
Achsvermessung
Lackierarbeiten
Hagel
Mietfahrzeug
Privat Kunden
Gewerbekubnden
Neueröffnung 01.03.2019 ganz wichtig
In 54392 Lindenau, Birkenstr 42 ist wichtig
Soll deuten das wir Karosserie Autolackiererei sind Unfall Schäden reparieren
der Banner hängt an einer sehr stark befahrener strße man soll es gleich sehen das wir ein karosserie 6 Autolackiererei sind ganz wichtig

```html
<!DOCTYPE html>
<html lang="de">
<head>
<meta charset="UTF-8">
<title>Karosserie &amp; Autolackiererei – Neueröffnung</title>
<link href="https://fonts.googleapis.com/css2?family=Roboto:wght@500;700&display=swap" rel="stylesheet">
<style>
  :root {
    --navy: #162032;
    --white: #ffffff;
    --blue: #1b9ad9;
  }
  * { margin: 0; padding: 0; box-sizing: border-box; }
  html, body { width: 800px; height: 1200px; overflow: hidden; background: var(--navy); }
  .banner {
    position: relative;
    width: 800px; height: 1200px;
    background: var(--navy);
    color: var(--white);
    font-family: "Roboto", Arial, sans-serif;
  }
  .banner__frame {
    position: absolute;
    left: 13px; top: 16px; width: 772px; height: 1169px;
    border: 1.5px solid var(--white);
  }
  .brand {
    position: absolute;
    left: 0; top: 168px; width: 800px;
    display: flex; align-items: center; justify-content: center;
    gap: 14px;
  }
  .brand__dot {
    width: 18px; height: 18px; border-radius: 50%;
    background: var(--blue); flex: none;
  }
  .brand__name {
    font-weight: 700; font-size: 32px; line-height: 40px;
    color: var(--white);
  }
  .headline {
    position: absolute; left: 0; width: 800px; text-align: center;
    font-weight: 700;
  }
  .headline--main { top: 335px; font-size: 73px; line-height: 80px; }
  .headline--sub { top: 413px; font-size: 49px; line-height: 56px; letter-spacing: -0.2px; }
  .services {
    position: absolute; left: 40px; top: 562px; list-style: none;
  }
  .services__item {
    position: absolute; left: 0; white-space: nowrap;
    display: flex; align-items: center;
    font-weight: 700; font-size: 22.7px; line-height: 30px;
  }
  .services__tick { width: 36px; height: 30px; margin-right: 12px; flex: none; }
  .opening {
    position: absolute; left: 418px; top: 577px; width: 334px; height: 199px;
    background: var(--blue);
    border: 1px solid #4fb5e8;
    text-align: center;
    padding-top: 56px;
  }
  .opening__label { font-weight: 500; font-size: 42px; line-height: 48px; }
  .opening__date { font-weight: 700; font-size: 37px; line-height: 44px; }
  .claim {
    position: absolute; left: 0; top: 918px; width: 800px; text-align: center;
    font-weight: 700; font-size: 37.5px; line-height: 42.5px;
  }
  .address {
    position: absolute; left: 0; top: 1095px; width: 800px; text-align: center;
    font-weight: 700; font-size: 22px; line-height: 26px;
  }
</style>
</head>
<body>
<div class="banner">
  <div class="banner__frame"></div>

  <div class="brand">
    <span class="brand__dot"></span>
    <span class="brand__name">Autolackiererei Berger</span>
  </div>

  <h1 class="headline headline--main">Karosserie</h1>
  <h2 class="headline headline--sub">&amp; Autolackiererei Meisterbetrieb</h2>

  <ul class="services">
    <li class="services__item" style="top:5px"><svg class="services__tick" viewBox="0 0 36 30"><path d="M2 15 L13 26 L34 4" fill="none" stroke="#1b9ad9" stroke-width="7"/></svg>Unfallinstandsetzung</li>
    <li class="services__item" style="top:53px"><svg class="services__tick" viewBox="0 0 36 30"><path d="M2 15 L13 26 L34 4" fill="none" stroke="#1b9ad9" stroke-width="7"/></svg>Fehlerdiagnose</li>
    <li class="services__item" style="top:99px"><svg class="services__tick" viewBox="0 0 36 30"><path d="M2 15 L13 26 L34 4" fill="none" stroke="#1b9ad9" stroke-width="7"/></svg>Achsvermessung</li>
    <li class="services__item" style="top:141px"><svg class="services__tick" viewBox="0 0 36 30"><path d="M2 15 L13 26 L34 4" fill="none" stroke="#1b9ad9" stroke-width="7"/></svg>Lackierarbeiten</li>
    <li class="services__item" style="top:187px"><svg class="services__tick" viewBox="0 0 36 30"><path d="M2 15 L13 26 L34 4" fill="none" stroke="#1b9ad9" stroke-width="7"/></svg>Hagel</li>
    <li class="services__item" style="top:228px"><svg class="services__tick" viewBox="0 0 36 30"><path d="M2 15 L13 26 L34 4" fill="none" stroke="#1b9ad9" stroke-width="7"/></svg>Mietfahrzeug</li>
  </ul>

  <div class="opening">
    <div class="opening__label">Neueröffnung</div>
    <div class="opening__date">01.03.2019</div>
  </div>

  <p class="claim">Soll deuten das wir Karosserie<br>Autolackiererei sind Unfall<br>Schäden reparieren</p>

  <p class="address">In 54392 Lindenau, Birkenstr 42</p>
</div>
</body>
</html>
```